New Label Design Project

DetailHi, we are a small Farm growing and selling fresh and dehydrated exotic vegetables to exotic market and ethnic restaurants. We plan to make changes our packaging by using clamshell instead of bags. This is why we send you this project. Our main Target Market are Jamaican, Haitian, Egyptian and Turkish restaurant. Small supermarket Markets like Zelto, Marcovina, Lunbrook Food Market, Quill food Market.... I sale to reseller in some farmers Market in Florida and Massachusetts. Then we have some direct customers they pick it at the farm stand. We don't have any online presence, my apologies... We are still working on that... We send you different logo. We are still working on the sizes of the clamshell. s for my new Label Design Project will be added soon.

```html
<!DOCTYPE html>
<html lang="en">
<head>
<meta charset="utf-8">
<title>Lowmeadow Growers – Clamshell Labels</title>
<link rel="stylesheet" href="https://fonts.googleapis.com/css2?family=Marcellus&family=Allura&family=Oswald:wght@400&family=Open+Sans:wght@400&display=swap">
<style>
  :root {
    --backdrop-light: #f4f5f4;
    --backdrop-dark: #d9dbda;
    --label-white: #ffffff;
    --ink: #2a2a2a;
    --script-green: #7aa05a;
    --grass-light: #8fd62a;
    --grass-mid: #55bf2a;
    --grass-deep: #2ea836;
    --text-on-green: #ffffff;
  }
  * { margin: 0; padding: 0; box-sizing: border-box; }
  html, body { width: 1200px; height: 1200px; overflow: hidden; }
  body {
    background: radial-gradient(ellipse at center, var(--backdrop-light) 0%, var(--backdrop-dark) 100%);
    position: relative;
    font-family: "Open Sans", sans-serif;
  }
  .label {
    position: absolute;
    width: 560px;
    height: 432px;
    background: var(--label-white);
    overflow: hidden;
  }
  .label--top-left { left: 31px; top: 139px; }
  .label--top-right { left: 607px; top: 139px; }
  .label--bottom-left { left: 31px; top: 617px; }
  .label--bottom-right { left: 607px; top: 617px; }

  .grower {
    position: absolute;
    right: 22px;
    top: 26px;
    display: flex;
    align-items: center;
    gap: 7px;
    font-family: "Open Sans", sans-serif;
    font-weight: 400;
    font-size: 14px;
    color: var(--ink);
  }
  .grower__mark {
    width: 10px; height: 10px;
    background: var(--ink);
  }

  .product {
    position: absolute;
    left: 0; right: 0;
    top: 108px;
    text-align: center;
    font-weight: 400;
  }
  .product__state {
    display: block;
    font-family: "Allura", cursive;
    font-size: 54px;
    line-height: 54px;
    color: var(--script-green);
    margin-bottom: -8px;
  }
  .product__name {
    display: block;
    font-family: "Marcellus", serif;
    font-size: 50px;
    line-height: 58px;
    color: var(--ink);
  }

  .meadow {
    position: absolute;
    left: 0; right: 0; bottom: 0;
    height: 200px;
    background:
      radial-gradient(ellipse at 50% 30%, var(--grass-light) 0%, transparent 60%),
      linear-gradient(180deg, var(--grass-mid) 0%, var(--grass-deep) 100%);
    clip-path: polygon(0 18%, 6% 8%, 12% 14%, 20% 4%, 28% 12%, 36% 2%, 44% 10%, 52% 0, 60% 9%, 68% 3%, 76% 12%, 84% 2%, 92% 10%, 100% 4%, 100% 100%, 0 100%);
  }

  .net-weight {
    position: absolute;
    left: 12px;
    bottom: 26px;
    width: 84px;
    text-align: center;
    color: var(--text-on-green);
    font-family: "Oswald", sans-serif;
    line-height: 1;
  }
  .net-weight__small { display: block; font-size: 10px; }
  .net-weight__value { display: block; font-size: 22px; margin: 3px 0 4px; font-family: "Open Sans", sans-serif; }

  .storage {
    position: absolute;
    left: 205px;
    bottom: 24px;
    font-family: "Oswald", sans-serif;
    font-size: 20px;
    line-height: 25px;
    color: var(--text-on-green);
  }
  .lot-box {
    position: absolute;
    left: 457px;
    bottom: 26px;
    width: 76px;
    height: 61px;
    background: var(--label-white);
  }
</style>
</head>
<body>

  <section class="label label--top-left">
    <div class="grower"><span class="grower__mark"></span>Lowmeadow Growers</div>
    <h2 class="product"><span class="product__state">Dehydrated</span><span class="product__name">Jute Leaves</span></h2>
    <div class="meadow" role="img" aria-label="Watercolour green grass meadow"></div>
    <div class="net-weight"><span class="net-weight__small">HOLDS</span><span class="net-weight__value">10oz</span><span class="net-weight__small">NET</span></div>
    <p class="storage">KEEP REFRIGERATED<br>GARDER RÉFRIGÉRÉ</p>
    <div class="lot-box"></div>
  </section>

  <section class="label label--top-right">
    <div class="grower"><span class="grower__mark"></span>Lowmeadow Growers</div>
    <h2 class="product"><span class="product__state">Fresh</span><span class="product__name">Sweet Purslane</span></h2>
    <div class="meadow" role="img" aria-label="Watercolour green grass meadow"></div>
    <div class="net-weight"><span class="net-weight__small">NET WT</span><span class="net-weight__value">120g</span><span class="net-weight__small">POIDS NET</span></div>
    <p class="storage">KEEP REFRIGERATED<br>GARDER RÉFRIGÉRÉ</p>
    <div class="lot-box"></div>
  </section>

  <section class="label label--bottom-left">
    <div class="grower"><span class="grower__mark"></span>Lowmeadow Growers</div>
    <h2 class="product"><span class="product__state">Fresh</span><span class="product__name">Jute Leaves</span></h2>
    <div class="meadow" role="img" aria-label="Watercolour green grass meadow"></div>
    <div class="net-weight"><span class="net-weight__small">NET WT</span><span class="net-weight__value">120g</span><span class="net-weight__small">POIDS NET</span></div>
    <p class="storage">KEEP REFRIGERATED<br>GARDER RÉFRIGÉRÉ</p>
    <div class="lot-box"></div>
  </section>

  <section class="label label--bottom-right">
    <div class="grower"><span class="grower__mark"></span>Lowmeadow Growers</div>
    <h2 class="product"><span class="product__state">Fresh</span><span class="product__name">Amaranth</span></h2>
    <div class="meadow" role="img" aria-label="Watercolour green grass meadow"></div>
    <div class="net-weight"><span class="net-weight__small">NET WT</span><span class="net-weight__value">120g</span><span class="net-weight__small">POIDS NET</span></div>
    <p class="storage">KEEP REFRIGERATED<br>GARDER RÉFRIGÉRÉ</p>
    <div class="lot-box"></div>
  </section>

</body>
</html>
```